New Artwork/Design for Established Weight Loss Podcast

Hello,
I would like new artwork/design for my podcast. It's called Bright Path Slimdown and has been a consistently top 50 show in the fitness/nutrition category on Orbix. My current design was originally created when I started the podcast over 2 years ago. It's time to refresh and update things! I would like a new design that incorporates a photo of me, but could also be used as a standalone logo for the podcast without my photo. A nice, clean, professional, yet fun design. Here is a Vantor drive link with professional photos that could be used:
https://files.example-share.net/folders/7Qkrt58x-p2mLWHtabvPXsaQ9Ro6JwZ3k?usp=sharing

Here's a little more about the show . There are three big taglines. These do NOT need to be included on the design. I just include them here to help with the feel/theme of the design.

1: To change your body, you must first change your brain.
2: There's so much more to you than just a number (what you weigh).
3: Losing weight is really about gaining life and living the life you've always wanted.

This podcast is all about busy moms, dads, husbands, wives who are working, raising kids, and trying to juggle everything life’s throwing at them … but also want to be the best they can for their family and friends and loved ones.

The podcast is NOT about how to get six-pack abs or how to drop as much weight as possible in 8 weeks. It's about finding sustainable success with your body, peace of mind with food, and improving your relationship with yourself.

Week by week, I provide bite-sized guidance - 20-25 minute episodes that pull back the curtain and reveal the truth about what it takes to lose weight and gain life - what strategy and approach real people are using to get results while escaping the soul-sucking, all-or-nothing diet mentality.

Here's a link to the current artwork: https://files.example-share.net/file/d/4T2bHn8qsvkeTrmzYpRd-ab3KNJ-m-QXZ/view?usp=sharing

And the logo without my photo: https://files.example-share.net/file/d/8JN5pKa3Rw_h2b74cFxYqPmE6zGtdLs/view?usp=sharing

I'm open to any colors, but something that either matches the colors of my website or signature "Move Glow Trim Down" program would probably be a smart idea. Here are links to my website and the MGTD logo . . .

Website: https://danemarshwellness.example/

MGTD logo:
https://files.example-share.net/file/d/5VQpLm2Kxe_Tw9Hr4zNgUa7YcBfsjdP/view?usp=sharing

Happy to answer any questions you might have. Thanks.

Target Market(s)

35 to 55 years old, roughly 70% female, 30% male, professionals, primarily in the U.S. and Canada

Industry/Entity Type

nutrition, health, weight loss

Requirements
Must have
• One version with my photo and the same design without my photo
Nice to have
• Open to any colors, but possibly incorporate colors from either my website or MGTD logo (see project description for more info)
Should not have
• Any hardcore fitness or bodybuilding imagery

```html
<!DOCTYPE html>
<html lang="en">
<head>
<meta charset="utf-8">
<title>Bright Path Slimdown — Podcast Cover</title>
<link rel="stylesheet" href="https://fonts.googleapis.com/css2?family=Bebas+Neue&family=Oswald:wght@200;600&display=swap">
<style>
  :root {
    --teal: #6ecacb;
    --white: #ffffff;
    --ink-top: #5b5b5b;
    --ink-mid: #1c1c1c;
    --ink-deep: #050505;
    --mic-grey: #6e6e6e;
    --band-teal: #4a7b7b;
    --band-dark: #1b2a2a;
  }
  html, body {
    margin: 0;
    padding: 0;
    width: 1200px;
    height: 1200px;
    overflow: hidden;
    background: #ffffff;
  }
  .cover {
    position: relative;
    width: 1200px;
    height: 1200px;
    background: linear-gradient(225deg, var(--ink-top) 0%, var(--ink-mid) 45%, var(--ink-deep) 100%);
    overflow: hidden;
  }
  .cover__stripe {
    position: absolute;
    left: 0;
    top: 0;
    width: 310px;
    height: 1200px;
    background: var(--teal);
  }
  .cover__byline-band {
    position: absolute;
    left: 350px;
    top: 959px;
    width: 850px;
    height: 104px;
    background: linear-gradient(90deg, rgba(74,123,123,0) 0%, var(--band-teal) 35%, #3f6c6c 70%, var(--band-dark) 100%);
  }
  .cover__host-photo {
    position: absolute;
    left: 36px;
    top: 100px;
    width: 354px;
    height: 1060px;
    border-radius: 12px;
    background: linear-gradient(180deg, #8a6a58 0%, #2e3036 22%, #2b2e33 50%, #23395a 70%, #1e3150 92%, #d8d6d0 100%);
  }
  .cover__art {
    position: absolute;
    inset: 0;
  }
  .title {
    font-family: "Bebas Neue", "Oswald", sans-serif;
  }
  .title--white { fill: var(--white); }
  .title--teal { fill: var(--teal); }
  .byline__with {
    font-family: "Oswald", sans-serif;
    font-weight: 200;
    fill: var(--white);
  }
  .byline__name {
    font-family: "Oswald", sans-serif;
    font-weight: 600;
    fill: var(--white);
  }
  .mic-icon {
    fill: none;
    stroke: var(--mic-grey);
    stroke-width: 9;
    stroke-linecap: round;
    stroke-linejoin: round;
  }
</style>
</head>
<body>
  <div class="cover">
    <div class="cover__stripe"></div>
    <div class="cover__byline-band"></div>
    <div class="cover__host-photo" role="img" aria-label="Full-length photo of the host smiling, in a charcoal hoodie, jeans and white sneakers, leaning on a black upright post"></div>

    <svg class="cover__art" width="1200" height="1200" viewBox="0 0 1200 1200" aria-label="Bright Path Slimdown with Dane Marsh">
      <text class="title title--white" x="436" y="331" font-size="228" textLength="689" lengthAdjust="spacingAndGlyphs">BRIGHT PATH</text>
      <text class="title title--teal" x="436" y="580" font-size="300" textLength="689" lengthAdjust="spacingAndGlyphs">SLIM</text>
      <text class="title title--white" x="436" y="865" font-size="356" textLength="505" lengthAdjust="spacingAndGlyphs">DOWN</text>

      <g class="mic-icon">
        <rect x="1008" y="622" width="92" height="160" rx="46"/>
        <line x1="1008" y1="662" x2="1036" y2="662"/>
        <line x1="1072" y1="662" x2="1100" y2="662"/>
        <line x1="1008" y1="686" x2="1036" y2="686"/>
        <line x1="1072" y1="686" x2="1100" y2="686"/>
        <line x1="1008" y1="710" x2="1036" y2="710"/>
        <line x1="1072" y1="710" x2="1100" y2="710"/>
        <line x1="1008" y1="734" x2="1100" y2="734"/>
        <path d="M987 740 v20 a67 67 0 0 0 134 0 v-20"/>
        <line x1="1042" y1="828" x2="1042" y2="852"/>
        <line x1="1066" y1="828" x2="1066" y2="852"/>
        <rect x="1000" y="852" width="108" height="14" rx="7"/>
      </g>

      <text class="byline__with" x="436" y="1048" font-size="84" textLength="128" lengthAdjust="spacingAndGlyphs">WITH</text>
      <text class="byline__name" x="598" y="1048" font-size="80" textLength="527" lengthAdjust="spacing" letter-spacing="10">DANE MARSH</text>
    </svg>
  </div>
</body>
</html>
```